Venture Capital Investment Firm

We are looking to overhaul our existing website (substantially), with only using the same logos (which we can provide).
We are an investment firm that focuses on making loans to late stage technology companies. Our site should ultimately look like other venture capital firms, and look modern and fresh. We have an existing website www.northvaleloan.com which this will be replacing, although we will be using a lot of the existing written content, and potentially the numbers of pages we will need, we are not wed to anything else. Please feel free to shoot any questions at any time and thank you in advance for your help!
Websites we like as examples:
https://www.tkbrandel.com/
https://www.emberwoodfunds.com/
Target Market(s)
Potential investors who will invest in our firm, as well as potentially companies that are looking to borrow money from us.

```html
<!DOCTYPE html>
<html lang="en">
<head>
<meta charset="utf-8">
<title>Northvale Investment Partners</title>
<link href="https://fonts.googleapis.com/css2?family=Montserrat:wght@400;600;700;800&family=Roboto:wght@300;400;500;700&family=Oswald:wght@500;600&family=Playball&display=swap" rel="stylesheet">
<style>
:root{
  --navy:#1d1936;
  --navy-2:#221d41;
  --blue:#2580b3;
  --blue-dark:#1f6f9c;
  --ink:#1b1b1b;
  --text:#6b6b6b;
  --muted:#9a9a9a;
  --grey:#efefef;
  --white:#ffffff;
}
*{box-sizing:border-box;margin:0;padding:0}
html,body{width:1200px;height:3561px;overflow:hidden}
body{position:relative;background:var(--white);font-family:"Roboto",sans-serif;color:var(--text)}
.abs{position:absolute}
.center{left:0;width:1200px;text-align:center}

/* top bar */
.topbar{top:0;left:0;width:1200px;height:21px;background:var(--navy);color:#d8d8e6;font-size:9px}
.topbar .addr{position:absolute;left:160px;top:5px}
.topbar .contact{position:absolute;left:700px;top:5px}
.topbar .contact span{margin-right:30px}
.topbar .socials{position:absolute;left:946px;top:5px;display:flex;gap:6px}
.topbar .socials i{width:10px;height:10px;background:#cfd0dc;display:block}

/* header */
.header{top:21px;left:0;width:1200px;height:80px;background:var(--white)}
.brand{position:absolute;left:160px;top:16px;display:flex;align-items:center;gap:12px}
.brand .dot{width:40px;height:40px;border-radius:50%;background:var(--ink)}
.brand .name{font-family:"Montserrat",sans-serif;font-weight:600;font-size:21px;color:var(--ink);line-height:1}
.brand .name small{display:block;font-size:7.5px;letter-spacing:.5px;margin-top:4px}
.nav{position:absolute;top:35px;left:596px;display:flex;font-family:"Roboto",sans-serif;font-size:12px;color:var(--ink)}
.nav a{color:inherit;text-decoration:none;margin-right:38px}
.nav a:last-child{margin-right:0}

/* hero */
.hero{top:101px;left:0;width:1200px;height:504px;background:linear-gradient(160deg,#3f6f88 0%,#9fc6de 45%,#e3eef6 55%,#5b86a3 75%,#1f3244 100%)}
.hero-title{top:431px;left:262px;width:637px;height:100px;background:rgba(40,40,48,.7);color:var(--white);font-family:"Oswald",sans-serif;font-weight:600;font-size:82px;letter-spacing:2px;text-align:center;line-height:100px}

/* section headings */
.script{font-family:"Playball",cursive;font-size:19px;color:var(--ink)}
.h2{font-family:"Montserrat",sans-serif;font-weight:700;font-size:21px;color:var(--ink)}
.rule{height:3px;width:40px;background:var(--blue);left:580px}
.lead{font-size:10.5px;line-height:18px;color:var(--text)}

/* story */
.tile{top:824px;height:194px}
.tile.who{left:160px;width:285px;background:linear-gradient(135deg,#c9c9cc,#ededef);box-shadow:8px 8px 0 var(--navy)}
.tile.who .icon{position:absolute;left:113px;top:46px;width:60px;height:60px;border:3px solid var(--navy);border-radius:50%}
.tile.who .label{position:absolute;left:0;width:285px;top:120px;text-align:center;font-family:"Montserrat",sans-serif;font-weight:700;font-size:14px;color:var(--navy)}
.photo{background:linear-gradient(135deg,#c9d3dc,#5c6570)}

/* stats */
.stats{top:1086px;left:0;width:1200px;height:201px;background:var(--blue)}
.stat{position:absolute;top:0;height:201px;width:180px;border-left:1px solid rgba(255,255,255,.18);text-align:center;color:var(--white)}
.stat b{display:block;margin-top:52px;font-family:"Montserrat",sans-serif;font-weight:800;font-size:50px;line-height:1}
.stat span{display:block;margin-top:22px;font-size:9.5px;letter-spacing:.5px}

/* services */
.service{width:260px;height:54px}
.service svg{position:absolute;left:0;top:0}
.service h4{position:absolute;left:55px;top:0;font-weight:400;font-size:10.5px;color:#444}
.service p{position:absolute;left:55px;top:15px;font-size:10.5px;line-height:17px;color:var(--muted)}
.divider{top:1563px;left:172px;width:848px;height:1px;background:#e4e4e4}

/* goal */
.goal-photo{top:1714px;left:0;width:459px;height:406px;background:linear-gradient(135deg,#9aa3ad,#d9dde2 50%,#6e7883)}
.goal-panel{top:1714px;left:459px;width:741px;height:406px;background:var(--grey)}
.goal-panel h3{position:absolute;left:55px;top:32px;font-family:"Montserrat",sans-serif;font-weight:700;font-size:22px;color:var(--ink)}
.goal-panel p{font-size:10.5px;line-height:18px;color:#555}
.step{position:absolute;left:55px;width:480px}
.step .num{position:absolute;left:0;top:0;width:48px;height:48px;border-radius:50%;background:var(--blue);border:3px solid var(--white);box-shadow:0 0 0 2px var(--blue);color:var(--white);font-family:"Montserrat",sans-serif;font-weight:700;font-size:22px;text-align:center;line-height:42px}
.step p{position:absolute;left:62px;top:6px;width:420px}

/* call band */
.callband{top:2120px;left:0;width:1200px;height:223px;background:var(--navy-2);color:#d6d6e4;text-align:center}
.callband .msg{margin-top:36px;font-weight:300;font-size:23px;line-height:29px}
.callband .phone{margin-top:14px;font-family:"Montserrat",sans-serif;font-weight:700;font-size:19px;color:var(--white);display:flex;justify-content:center;align-items:center;gap:6px}
.callband .down{position:absolute;left:585px;top:168px;width:30px;height:30px;border-radius:50%;background:var(--blue)}

/* team */
.team-title{top:2383px;font-family:"Montserrat",sans-serif;font-weight:700;font-size:25px;color:var(--ink)}
.member{top:2551px;width:242px;height:330px;background:linear-gradient(180deg,#cfd4da,#3b4a63)}
.member .social{position:absolute;right:0;top:0;width:26px;height:108px;background:var(--blue)}
.member .social i{display:block;width:10px;height:10px;border-radius:50%;background:#cfe3f0;margin:10px auto 15px}
.member .tag{position:absolute;left:-10px;top:270px;width:140px;height:38px;background:var(--navy-2);color:var(--white);padding:7px 0 0 22px}
.member .tag b{display:block;font-family:"Montserrat",sans-serif;font-size:10px}
.member .tag span{font-size:8px;color:#c9c9d8}

/* consulting */
.consult{top:2955px;left:0;width:1200px;height:268px;background:linear-gradient(90deg,#e6e6e8,#d9dadd)}
.consult h3{position:absolute;left:160px;top:64px;font-family:"Montserrat",sans-serif;font-weight:700;font-size:20px;color:var(--navy-2)}
.consult p{position:absolute;left:160px;top:96px;font-size:10.5px;color:#555}
.consult .btn{position:absolute;left:765px;top:60px;width:273px;height:45px;background:var(--navy-2);color:var(--white);font-family:"Montserrat",sans-serif;font-weight:700;font-size:14px;line-height:45px;padding-left:30px}

/* footer */
.footer{top:3223px;left:0;width:1200px;height:338px;background:var(--navy)}
.newsletter{top:3134px;left:160px;width:878px;height:174px;background:var(--blue);text-align:center;color:var(--white)}
.newsletter h3{margin-top:24px;font-family:"Montserrat",sans-serif;font-weight:700;font-size:24px}
.newsletter p{margin-top:5px;font-size:11px}
.newsletter .form{position:absolute;left:200px;top:98px;display:flex}
.newsletter .field{width:352px;height:40px;background:var(--white);color:#aaa;font-size:10px;text-align:left;padding:13px 0 0 14px}
.newsletter .submit{width:110px;height:40px;background:var(--navy-2);font-size:14px;line-height:40px}
.join{top:3336px;font-family:"Roboto",sans-serif;font-weight:500;font-size:35px;color:var(--white)}
.circles{top:3399px;left:478px;display:flex;gap:12px}
.circles i{width:33px;height:33px;border:2px solid #8a88a6;border-radius:50%;display:block}
.foot-nav{top:3487px;font-size:10px;color:#c7c6d8;letter-spacing:.5px}
.foot-nav span{margin:0 16px}
.copy{top:3520px;font-size:9.5px;color:#c7c6d8}
</style>
</head>
<body>

<div class="abs topbar">
  <span class="addr">&#9679; 220 Harbor Lane #310 Oakdale, CA 94000</span>
  <div class="contact"><span>&#9742; 555-210-3400</span><span>&#9993; inquiries@northvaleloan.com</span></div>
  <div class="socials"><i></i><i></i><i></i><i></i><i></i></div>
</div>

<header class="abs header">
  <div class="brand">
    <div class="dot"></div>
    <div class="name">Northvale<small>INVESTMENT PARTNERS, LLC</small></div>
  </div>
  <nav class="nav">
    <a href="#">HOME</a><a href="#">STRATEGY</a><a href="#">ABOUT US</a><a href="#">TEAM</a><a href="#">NEWS</a><a href="#">CONTACT</a>
  </nav>
</header>

<div class="abs hero" role="img" aria-label="Upward view of glass skyscrapers against a blue sky"></div>
<div class="abs hero-title">INVESMENT FIRM</div>

<section>
  <div class="abs center script" style="top:637px">What we do</div>
  <h2 class="abs center h2" style="top:666px">STORY ABOUT US</h2>
  <div class="abs rule" style="top:705px"></div>
  <p class="abs center lead" style="top:738px;left:210px;width:780px">Lorem Ipsum is simply dummy text of the printing and typesetting industry. Lorem Ipsum has been the industry's standard dummy text ever since the 1500s, when an unknown printer took a galley of type and scrambled it to make a type specimen book. It has survived not only five centuries, but also the Ipsum passages, and more recently with desktop publishing software like Folio Press including versions of Lorem Ipsum.</p>
  <div class="abs tile who"><div class="icon"></div><div class="label">WHO WE ARE</div></div>
  <div class="abs tile photo" style="left:466px;width:276px" role="img" aria-label="Business team meeting around a table"></div>
  <div class="abs tile photo" style="left:762px;width:276px" role="img" aria-label="Smiling colleagues in an office"></div>
</section>

<section class="abs stats">
  <div class="stat" style="left:155px"><b>42</b><span>PROJECTS</span></div>
  <div class="stat" style="left:333px"><b>123</b><span>HAPPY CLIENT</span></div>
  <div class="stat" style="left:514px"><b>15</b><span>AWARD WINNER</span></div>
  <div class="stat" style="left:696px"><b>99</b><span>CUP OF COFFEE</span></div>
  <div class="stat" style="left:876px;border-right:1px solid rgba(255,255,255,.18)"><b>24</b><span>MEMBERS</span></div>
</section>

<section>
  <div class="abs center script" style="top:1324px">We Offers</div>
  <h2 class="abs center h2" style="top:1353px">AMAZING SERVICES</h2>
  <div class="abs rule" style="top:1387px"></div>
  <p class="abs center lead" style="top:1410px;font-size:12.5px">Lorem Ipsum is simply dummy text of the printing and typesetting industry.</p>

  <div class="abs service" style="left:160px;top:1476px">
    <svg width="46" height="40" viewBox="0 0 46 40"><rect x="6" y="4" width="34" height="20" rx="2" fill="none" stroke="#1d1936" stroke-width="3" transform="rotate(-12 23 14)"/><rect x="2" y="16" width="34" height="20" rx="2" fill="#fff" stroke="#1d1936" stroke-width="3"/><rect x="2" y="21" width="34" height="4" fill="#1d1936"/></svg>
    <h4>STRUCTURED CREDIT</h4><p>Lorem Ipsum is simply dummy text<br>Ipsum has been the industry's standard</p>
  </div>
  <div class="abs service" style="left:464px;top:1476px">
    <svg width="46" height="40" viewBox="0 0 46 40"><path d="M4 10 L14 22 L23 6 L32 22 L42 10 L38 34 H8 Z" fill="none" stroke="#1d1936" stroke-width="3" stroke-linejoin="round"/><circle cx="16" cy="28" r="2" fill="#1d1936"/><circle cx="23" cy="28" r="2" fill="#1d1936"/><circle cx="30" cy="28" r="2" fill="#1d1936"/></svg>
    <h4>MILESTONES &amp; ROYALTIES</h4><p>Lorem Ipsum is simply dummy text<br>Ipsum has been the industry's standard</p>
  </div>
  <div class="abs service" style="left:764px;top:1476px">
    <svg width="46" height="40" viewBox="0 0 46 40"><rect x="6" y="4" width="30" height="30" rx="2" fill="none" stroke="#1d1936" stroke-width="3"/><line x1="11" y1="14" x2="31" y2="14" stroke="#1d1936" stroke-width="2"/><line x1="11" y1="20" x2="31" y2="20" stroke="#1d1936" stroke-width="2"/><circle cx="34" cy="30" r="8" fill="#fff" stroke="#1d1936" stroke-width="3"/></svg>
    <h4>LEGACY ASSETS</h4><p>Lorem Ipsum is simply dummy text<br>Ipsum has been the industry's standard</p>
  </div>

  <div class="abs divider"></div>

  <div class="abs service" style="left:160px;top:1597px">
    <svg width="46" height="40" viewBox="0 0 46 40"><rect x="4" y="24" width="6" height="12" fill="#1d1936"/><rect x="13" y="18" width="6" height="18" fill="#1d1936"/><rect x="22" y="12" width="6" height="24" fill="#1d1936"/><rect x="31" y="6" width="6" height="30" fill="#1d1936"/><line x1="2" y1="38" x2="42" y2="38" stroke="#1d1936" stroke-width="2"/></svg>
    <h4>INVESTED BY OUR PARTNERS</h4><p>Lorem Ipsum is simply dummy text<br>Ipsum has been the industry's standard</p>
  </div>
  <div class="abs service" style="left:464px;top:1597px">
    <svg width="46" height="40" viewBox="0 0 46 40"><text x="6" y="36" font-family="Montserrat,sans-serif" font-weight="800" font-size="40" fill="#1d1936">$</text></svg>
    <h4>INNOVATING FINANCING STRUCTURES</h4><p>Lorem Ipsum is simply dummy text<br>Ipsum has been the industry's standard</p>
  </div>
  <div class="abs service" style="left:764px;top:1597px">
    <svg width="46" height="40" viewBox="0 0 46 40"><circle cx="22" cy="20" r="12" fill="none" stroke="#1d1936" stroke-width="3"/><circle cx="22" cy="20" r="4" fill="#1d1936"/><circle cx="8" cy="8" r="3" fill="#1d1936"/><circle cx="36" cy="8" r="3" fill="#1d1936"/><circle cx="8" cy="34" r="3" fill="#1d1936"/><circle cx="36" cy="34" r="3" fill="#1d1936"/></svg>
    <h4>TECHNOLOGY INVESTMENTS</h4><p>Lorem Ipsum is simply dummy text<br>Ipsum has been the industry's standard</p>
  </div>
</section>

<section>
  <div class="abs goal-photo" role="img" aria-label="Hands typing on a laptop at a desk with a coffee cup"></div>
  <div class="abs goal-panel">
    <h3>OUR GOAL</h3>
    <p style="position:absolute;left:55px;top:68px;width:520px">Lorem Ipsum is simply dummy text of the printing and typesetting industry. Lorem Ipsum has been type and scrambled it to make a type specimen book. It has survived not only five centuries, but also the leap publishing software like Folio Press including versions of Lorem Ipsum.</p>
    <div class="step" style="top:142px"><div class="num">1</div><p>Lorem Ipsum is simply dummy text of the printing and typesetting industry.<br>Lorem Ipsum has been the industry's standard dummy text</p></div>
    <div class="step" style="top:205px"><div class="num">2</div><p>Lorem Ipsum is simply dummy text of the printing and typesetting industry.<br>Lorem Ipsum has been the industry's standard dummy text</p></div>
    <div class="step" style="top:268px"><div class="num">3</div><p>Lorem Ipsum is simply dummy text of the printing and typesetting industry.<br>Lorem Ipsum has been the industry's standard dummy text</p></div>
    <p style="position:absolute;left:55px;top:336px;width:520px">Lorem Ipsum is simply dummy text of the printing and typesetting industry. Lorem Ipsum has been the industry's standard dummy text ever since scrambled it to make a type specimen book.</p>
  </div>
</section>

<section class="abs callband">
  <div class="msg">We are ready to manage<br>investment finance of any complexity.Call us now!</div>
  <div class="phone"><svg width="16" height="16" viewBox="0 0 24 24"><path d="M6.6 10.8a15 15 0 0 0 6.6 6.6l2.2-2.2a1 1 0 0 1 1-.25 11.4 11.4 0 0 0 3.6.57 1 1 0 0 1 1 1V20a1 1 0 0 1-1 1A17 17 0 0 1 3 4a1 1 0 0 1 1-1h3.5a1 1 0 0 1 1 1c0 1.25.2 2.450.57 3.57a1 1 0 0 1-.25 1z" fill="#fff"/></svg>+1 555 014 2287</div>
  <div class="down"><svg width="30" height="30" viewBox="0 0 30 30"><path d="M10 13 L15 18 L20 13" fill="none" stroke="#1d1936" stroke-width="2.5"/></svg></div>
</section>

<section>
  <h2 class="abs center team-title">OUR TEAM</h2>
  <svg class="abs" style="top:2428px;left:322px" width="556" height="18" viewBox="0 0 556 18">
    <line x1="0" y1="6" x2="240" y2="6" stroke="#d0d0d0"/><line x1="0" y1="10" x2="240" y2="10" stroke="#d0d0d0"/>
    <line x1="316" y1="6" x2="556" y2="6" stroke="#d0d0d0"/><line x1="316" y1="10" x2="556" y2="10" stroke="#d0d0d0"/>
    <polygon points="258,4 260,8 264,8 261,11 262,15 258,12 254,15 255,11 252,8 256,8" fill="#1d1936"/>
    <polygon points="278,0 281,6 287,6 282,10 284,16 278,12 272,16 274,10 269,6 275,6" fill="#2580b3"/>
    <polygon points="298,4 300,8 304,8 301,11 302,15 298,12 294,15 295,11 292,8 296,8" fill="#1d1936"/>
  </svg>
  <p class="abs center lead" style="top:2467px;left:220px;width:760px">Lorem Ipsum is simply dummy text of the printing and typesetting industry. Lorem Ipsum has been the industry's standard dummy text ever since the 1500s, and more recently with desktop publishing software like Folio Press including versions of Lorem Ipsum</p>

  <div class="abs member" style="left:171px" role="img" aria-label="Portrait of a team member in a dark suit">
    <div class="social"><i></i><i></i><i></i></div>
    <div class="tag"><b>DANIEL HARLOW</b><span>Lorem Ipsum is simply</span></div>
  </div>
  <div class="abs member" style="left:482px" role="img" aria-label="Portrait of a smiling team member in a grey blazer">
    <div class="social"><i></i><i></i><i></i></div>
    <div class="tag"><b>CLARA BENNING</b><span>Lorem Ipsum is simply</span></div>
  </div>
  <div class="abs member" style="left:785px" role="img" aria-label="Portrait of a smiling team member in a grey suit">
    <div class="social"><i></i><i></i><i></i></div>
    <div class="tag"><b>MARTIN OAKES</b><span>Lorem Ipsum is simply</span></div>
  </div>
</section>

<section class="abs consult">
  <h3>CONSULTING SERVICE</h3>
  <p>We are providing wide range of Consulting Services &amp; World wide happy Clients</p>
  <div class="btn">START YOUR PROJECT NOW &nbsp;&#10095;</div>
</section>

<footer>
  <div class="abs footer"></div>
  <div class="abs newsletter">
    <h3>NEWSLETTER</h3>
    <p>Enter your email adress for getting updates</p>
    <div class="form"><div class="field">Enter your email id</div><div class="submit">Subscribe</div></div>
  </div>
  <div class="abs center join">Join the conversation</div>
  <div class="abs circles"><i></i><i></i><i></i><i></i><i></i></div>
  <div class="abs center foot-nav">HOME<span>|</span>STRATEGY<span>|</span>ABOUT US<span>|</span>TEAM<span>|</span>NEWS<span>|</span>CONTACT US</div>
  <div class="abs center copy">© 2020 Northvale Investment Partners LLC. All Rights Reserved.</div>
</footer>

</body>
</html>
```